Partnering collective needs a range of stationary to match with a logo

My business group is a collective of Partnership brokers. We would with organisations that are trying to collaborate or partner more effectively, and we support conversations about power, control, equity, transparency, and fit-for-purposes processes for better collaboration. We had a logo developed by a designer on this site a few years ago. We now need the following, to go with the logo:
1. A Powerpoint presentation template. This template should utilise the logo and colours, and should give a range of options for slide layout in a Master slide set, including slides with images/pictures. It would be good if the colour palette varied throughout the slide, or through the slide options. We often work in situations where people are having challenging and difficult conversations, so the presentation of the Powerpoint needs to be calming and reflective, even though the colours we are using are quite vibrant.
2. A report template using the logo, which allows us to have a cover page, and the logo in either a head/footer or as a watermark on a page throughout the rest of the document. We often write bids or proposals, which we would use this layout for. We also write reports and partnering agreement documents, which we would use this document for.
3. A letterhead using our logo, for professional looking letters. We don't have one business address, there are a few of us using the logo in different locations, so we would need a letter template that allows us to input our own address/details.
Thank you!

We work with NGos, government departments, scientists, private sector, health and education institutions, academics.

• Calibri

• So far the designs I have received have been too corporate looking. What we do is almost like counselling, except between organisations, not individuals. The powerpoint template needs to look gentle, calming, soothin, rather than dynamic and aggressive. Would be good to use more of the light blues and maroon in the logo, not such overpowering orange. f
• The powerpoint template doesn't need to have corporate slides. graphs, profit projections, market analysis, that kind of thing. We don't do corporate work. We do people to people work. Most or our slides will just have text and photos.

```html
<!DOCTYPE html>
<html lang="en">
<head>
<meta charset="utf-8">
<title>Bridgewell Alliance Letterhead</title>
<link rel="stylesheet" href="https://fonts.googleapis.com/css2?family=Catamaran:wght@600;700&family=Arimo:wght@400&display=swap">
<style>
  :root {
    --backdrop: #b4b1b0;
    --paper: #ffffff;
    --navy: #173c69;
    --orange: #f6962f;
    --ink: #4d4d4f;
    --white: #ffffff;
  }
  * { margin: 0; padding: 0; box-sizing: border-box; }
  html, body {
    width: 1144px; height: 1200px; overflow: hidden;
    background: var(--backdrop);
  }
  .letterhead {
    position: absolute; left: 148px; top: 0;
    width: 848px; height: 1200px;
    background: var(--paper);
    overflow: hidden;
    color: var(--ink);
  }
  .brand {
    position: absolute; left: 77px; top: 96px;
    display: flex; align-items: center; gap: 12px;
  }
  .brand-dot {
    width: 22px; height: 22px; border-radius: 50%;
    background: var(--navy);
  }
  .brand-name {
    font-family: "Catamaran", sans-serif; font-weight: 700;
    font-size: 28px; line-height: 1; color: var(--navy);
    padding-top: 4px;
  }
  .greeting {
    position: absolute; left: 77px; top: 368px;
    font-family: "Catamaran", sans-serif; font-weight: 700;
    font-size: 20px; color: var(--ink);
  }
  .letter-body {
    position: absolute; left: 77px; top: 424px; width: 700px;
    font-family: "Arimo", sans-serif; font-size: 14.1px; line-height: 17.5px;
    color: var(--ink); white-space: nowrap;
  }
  .letter-body p { margin-bottom: 15px; }
  .closing {
    position: absolute; left: 77px; top: 783px;
    font-family: "Catamaran", sans-serif; font-weight: 700;
    font-size: 11px; color: var(--ink);
  }
  .signature {
    position: absolute; left: 77px; top: 832px;
    width: 139px; height: 42px;
    background: linear-gradient(90deg, #e6e6e7, #f1f1f2);
    border-radius: 4px;
  }
  .footer-band {
    position: absolute; left: 0; top: 1090px; width: 848px; height: 75px;
    background: var(--navy);
  }
  .footer-accent {
    position: absolute; left: 759px; top: 1090px; width: 89px; height: 75px;
    background: var(--orange);
  }
  .footer-disc {
    position: absolute; left: 637px; top: 1062px;
    width: 132px; height: 132px; border-radius: 50%;
    background: var(--white);
  }
  .contact-list {
    position: absolute; left: 51px; top: 1100px;
    list-style: none;
    font-family: "Arimo", sans-serif; font-size: 13px; line-height: 16.5px;
    color: var(--white);
  }
  .contact-list li { display: flex; align-items: center; gap: 6px; }
  .contact-list svg { width: 10px; height: 10px; fill: var(--white); }
  .footer-divider {
    position: absolute; left: 221px; top: 1103px; width: 1px; height: 48px;
    background: var(--white);
  }
  .address {
    position: absolute; left: 239px; top: 1100px;
    font-family: "Arimo", sans-serif; font-size: 13px; line-height: 16.5px;
    color: var(--white); font-style: normal;
  }
</style>
</head>
<body>
<main class="letterhead">
  <div class="brand">
    <span class="brand-dot" aria-hidden="true"></span>
    <span class="brand-name">Bridgewell Alliance</span>
  </div>

  <h1 class="greeting">Dear Mr. Smith,</h1>

  <div class="letter-body">
    <p>Lorem ipsum dolor sit amet, consectetuer adipiscing elit, sed diam nonmmy nibh euismod tincidunt ut laor<br>eet dolore magna aliquam erat volutpat. Ut wisi enim ad minim veniam, quis nostrud exerci tationmcorper<br>suscipit lobortis nisl ut aliquip ex ea commodo consequat. Duis autem vel eum iriure dolor in hendrerit in<br>vulputate velit esse molestie consequat, vel illum dolore eu feugiat</p>
    <p>Rorem ipsum dolor sit amet, consectetuer adipiscing elit, sed diam nonmmy nibh euismod tincidunt ut laor<br>eet dolore magna aliquam erat volutpat. Ut wisi enim ad minim veniam, quis nostrud exerci tationmcorper<br>suscipit lobortis nisl ut aliquip ex ea commodo consequat. Duis autem vel eum iriure dolor in hendrerit in<br>vulputate velit esse molest</p>
    <p>Dorem ipsum dolor sit amet, consectetuer adipiscing elit, sed diam nonmmy nibh euismod tincidunt ut laor<br>eet dolore magna aliquam erat volutpat. Ut wisi enim ad minim veniam, quis nostrud exerci tationmcorper<br>suscipit lobortis nisl ut aliquip ex ea commodo consequat. Duis autem vel eum iriure dolor in hendrerit in<br>suscipit lobortis nisl ut aliquip ex ea commodo consequat. Duis autem vel eum iriure dolor in hendrerit in<br>vulputate velit esse molestie consequat, vel illum</p>
    <p>Sorem ipsum dolor sit amet, consectetuer adipiscing elit, sed diam nonmmy nibh euismod tincidunt ut laor<br>eet dolore magna aliquam erat volutpat. Ut wisi enim ad minim veniam, quis nostrud exerci tationmcorper<br>suscipit lobortis nisl ut aliquip ex ea commodo consequat. Duis autem vel eum iriure dolor in</p>
  </div>

  <p class="closing">Sincerely,</p>
  <div class="signature" role="img" aria-label="Handwritten signature of the sender"></div>

  <footer>
    <div class="footer-band"></div>
    <div class="footer-accent"></div>
    <div class="footer-disc" aria-hidden="true"></div>
    <ul class="contact-list">
      <li><svg viewBox="0 0 10 10" aria-hidden="true"><path d="M2 0.5l1.6 2.2-0.9 1.1c0.6 1.3 1.4 2.1 2.6 2.6l1.1-0.9 2.2 1.6-0.8 1.9C4.6 9.2 0.7 5.3 0.3 1.3z"/></svg>123-456-2100</li>
      <li><svg viewBox="0 0 10 10" aria-hidden="true"><path d="M0.5 2h9v6h-9z M1 2.5l4 3 4-3" stroke="#173c69" stroke-width="0.8"/></svg>youremail@gmail.com</li>
      <li><svg viewBox="0 0 10 10" aria-hidden="true"><circle cx="5" cy="5" r="4.5"/></svg>www.yourwebsite.com</li>
    </ul>
    <div class="footer-divider"></div>
    <address class="address">Your address<br>city<br>state, ZIP 0000</address>
  </footer>
</main>
</body>
</html>
```